tax advisory service business cards
Professional
Loretta Fenwick
Tax Advisory Specialist
51924 HOLLISTER LANE SUITE C
MARROWFIELD, MS 70812
FISCAL9COUNSELDESK@QUILLMAIL.COM
FCD4FILE.COM

```html
<!DOCTYPE html>
<html lang="en">
<head>
<meta charset="utf-8">
<title>Fiscal Counsel Desk – Business Cards</title>
<link href="https://fonts.googleapis.com/css2?family=Libre+Baskerville:ital,wght@0,700;1,400&family=Open+Sans:wght@400;600&display=swap" rel="stylesheet">
<style>
  :root{
    --navy:#152550;
    --navy-deep:#0d1a3d;
    --gold:#c9a94c;
    --gold-light:#e2c878;
    --paper:#ffffff;
    --paper-shade:#e6e8ec;
    --ink:#3a3d45;
    --ink-soft:#5b5f68;
    --backdrop:#d9dbe0;
  }
  *{margin:0;padding:0;box-sizing:border-box}
  html,body{width:1200px;height:901px;overflow:hidden}
  body{background:var(--backdrop);font-family:"Open Sans",Arial,sans-serif;position:relative}

  .card{position:absolute;width:540px;height:309px;border-radius:16px;overflow:hidden;
        box-shadow:0 10px 28px rgba(0,0,0,.25)}
  .card--back{left:45px;top:296px;background:linear-gradient(160deg,#1d2f62 0%,var(--navy) 45%,var(--navy-deep) 100%)}
  .card--front{left:615px;top:296px;background:linear-gradient(165deg,var(--paper) 0%,#f4f5f7 55%,var(--paper-shade) 100%)}

  /* back */
  .back-mark{position:absolute;left:50%;top:62px;transform:translateX(-50%);width:118px;height:118px;
             border-radius:50%;background:var(--gold);border:4px solid var(--gold-light)}
  .back-name{position:absolute;left:0;right:0;top:198px;text-align:center;color:var(--paper);
             font-family:"Libre Baskerville",Georgia,serif;font-weight:700;font-size:19px;letter-spacing:.5px}
  .back-web{position:absolute;left:0;right:0;bottom:26px;text-align:center;color:#8f9bbd;
            font-size:11px;letter-spacing:4px}

  /* front */
  .brand{position:absolute;left:0;right:0;top:24px;text-align:center}
  .brand-mark{display:block;margin:0 auto 6px;width:40px;height:40px;border-radius:50%;background:var(--navy);
              border:3px solid var(--gold)}
  .brand-name{font-family:"Libre Baskerville",Georgia,serif;font-weight:700;font-size:16px;color:var(--navy);letter-spacing:.3px}
  .brand-tagline{font-family:"Libre Baskerville",Georgia,serif;font-style:italic;font-size:7.5px;color:var(--ink-soft);margin-top:2px}

  .bands{position:absolute;left:0;top:0}

  .person{position:absolute;right:24px;top:170px;text-align:right}
  .person-name{font-size:15px;color:var(--ink)}
  .person-title{font-size:9.5px;color:var(--ink-soft);margin-top:1px}

  .band-web{position:absolute;right:24px;top:210px;color:var(--paper);font-size:10px;letter-spacing:3px}

  .address{position:absolute;left:22px;top:232px;font-size:11px;line-height:16px;color:var(--ink-soft);font-style:normal}
  .divider{position:absolute;left:207px;top:234px;width:1px;height:36px;background:#b6b9c0}
  .contact{position:absolute;left:218px;top:232px;font-size:11px;line-height:16px;color:var(--ink-soft)}
  .contact-row{display:flex;align-items:center;gap:6px}
  .contact-row svg{flex:none}
</style>
</head>
<body>

  <section class="card card--back" aria-label="Card back">
    <div class="back-mark"></div>
    <div class="back-name">Fiscal Counsel Desk, Inc.</div>
    <div class="back-web">www.fcd4file.com</div>
  </section>

  <section class="card card--front" aria-label="Card front">
    <svg class="bands" width="540" height="309" viewBox="0 0 540 309">
      <polygon points="0,150 180,150 190,168 0,168" fill="var(--gold)"/>
      <polygon points="196,206 540,206 540,226 208,226" fill="var(--navy)"/>
    </svg>

    <header class="brand">
      <span class="brand-mark"></span>
      <div class="brand-name">FISCAL COUNSEL DESK, INC.</div>
      <div class="brand-tagline">We Prepare and Review Every Return With Care</div>
    </header>

    <div class="person">
      <div class="person-name">Loretta Fenwick</div>
      <div class="person-title">Tax Advisory Specialist</div>
    </div>
    <div class="band-web">www.fcd4file.com</div>

    <address class="address">
      51924 Hollister Lane Suite B<br>
      Marrowfield, MS 70812
    </address>
    <div class="divider"></div>
    <div class="contact">
      <div class="contact-row">
        <svg width="11" height="11" viewBox="0 0 24 24"><path fill="var(--gold)" d="M6.6 10.8a15 15 0 0 0 6.6 6.6l2.2-2.2a1 1 0 0 1 1-.25 11.4 11.4 0 0 0 3.6.57 1 1 0 0 1 1 1V20a1 1 0 0 1-1 1A17 17 0 0 1 3 4a1 1 0 0 1 1-1h3.5a1 1 0 0 1 1 1c0 1.25.2 2.45.57 3.6a1 1 0 0 1-.25 1z"/></svg>
        <span>731-555-0148</span>
      </div>
      <div class="contact-row">
        <svg width="11" height="9" viewBox="0 0 24 18"><rect x="1" y="1" width="22" height="16" rx="2" fill="none" stroke="var(--gold)" stroke-width="2"/><path d="M1 2l11 8 11-8" fill="none" stroke="var(--gold)" stroke-width="2"/></svg>
        <span>fiscal9counseldesk@quillmail.com</span>
      </div>
    </div>
  </section>

</body>
</html>
```